Bright Wallet Blueprint: 8 Simple Moves To Put Your Cash Affairs Straight

Need a book cover for a book called "Bright Wallet Blueprint: 8 Moves To Put Your Cash Affairs Straight"

The book is 5.5 by 8.5 and has no spine.

I am attaching the current cover but would like to see some other options that you all can come up with.

This book contains 8 specific action items for what people need to do.
Pay down debt. get estate documents in order. Be careful when buying a house, have enough life insurance to pay debt...etc.

Target Market(s)

Target market is parents around 35-55 years old who are concerned about their financial situation.

Industry/Entity Type

Financial Planning

Font styles to use
Serif

Colors

Designer to choose colors to be used in the design.

Requirements
Must have
• Definitely want my picture on the back.
Nice to have
• I'm pretty much open to ideas.

```html
<!DOCTYPE html>
<html lang="en">
<head>
<meta charset="utf-8">
<title>Bright Wallet Blueprint — Book Cover</title>
<link rel="stylesheet" href="https://fonts.googleapis.com/css2?family=Bebas+Neue&family=Oswald:wght@400;600&display=swap">
<style>
  :root {
    --paper: #ffffff;
    --title-red: #f00a0a;
    --ink: #333333;
    --wood: #eac3a6;
    --coin-light: #e6cf8f;
    --coin-mid: #c9a555;
    --coin-dark: #9a7a36;
  }
  html, body {
    margin: 0;
    padding: 0;
    overflow: hidden;
    background: var(--paper);
  }
  .cover {
    position: relative;
    width: 777px;
    height: 1200px;
    background: var(--paper);
    overflow: hidden;
  }
  .cover-photo {
    position: absolute;
    left: 322px;
    top: 408px;
    width: 400px;
    height: 636px;
    border-radius: 6px;
    background: linear-gradient(180deg, var(--wood) 0%, #efe0cf 30%, var(--coin-light) 36%, var(--coin-mid) 70%, var(--coin-dark) 100%);
  }
  .title-graphic {
    position: absolute;
    left: 0;
    top: 0;
    width: 777px;
    height: 400px;
  }
  .title-main {
    font-family: "Bebas Neue", "Oswald", sans-serif;
    fill: var(--title-red);
  }
  .title-second {
    font-family: "Oswald", sans-serif;
    font-weight: 600;
    fill: var(--ink);
  }
  .rise-arrow {
    fill: none;
    stroke: var(--ink);
    stroke-width: 9;
    stroke-linecap: round;
    stroke-linejoin: round;
  }
  .subtitle {
    position: absolute;
    left: 60px;
    top: 404px;
    margin: 0;
    font-family: "Oswald", sans-serif;
    font-weight: 400;
    font-size: 58px;
    line-height: 92px;
    letter-spacing: -3px;
    color: var(--ink);
    transform: scaleX(0.8);
    transform-origin: left top;
  }
  .subtitle span { display: block; }
  .author {
    position: absolute;
    left: 0;
    top: 1058px;
    width: 777px;
    height: 90px;
  }
  .author text {
    font-family: "Bebas Neue", "Oswald", sans-serif;
    fill: var(--ink);
  }
</style>
</head>
<body>
<main class="cover">
  <div class="cover-photo" role="img" aria-label="Photo of a small wooden house model resting on a tall stack of gold coins"></div>

  <svg class="title-graphic" viewBox="0 0 777 400" aria-label="Bright Wallet Blueprint">
    <text class="title-main" x="116" y="216" font-size="215" textLength="624" lengthAdjust="spacingAndGlyphs">BRIGHT WALLET</text>
    <text class="title-second" x="36" y="346" font-size="150" textLength="396" lengthAdjust="spacingAndGlyphs">Blueprint</text>
    <path class="rise-arrow" d="M184 358 C 330 390, 560 378, 690 268"/>
    <path class="rise-arrow" d="M648 268 L 692 264 L 680 306"/>
  </svg>

  <p class="subtitle">
    <span>8 Moves</span>
    <span>To Put Your</span>
    <span>Cash Affairs</span>
    <span>Straight</span>
  </p>

  <svg class="author" viewBox="0 0 777 90" aria-label="Jack Sandover">
    <text x="124" y="76" font-size="80" textLength="540" lengthAdjust="spacing">JACK SANDOVER</text>
  </svg>
</main>
</body>
</html>
```